Cause bitches need love too!

I am creating an ad campaign. It will be a series of featured dogs in our shelter and they will contain a picture of the dog wich should be big enough to see on a yard sign and will change every week. I am placing the signs so that they lead you to the shelter. This is why I am also including the copy that says "you're almost there".

I have 4 tag lines:

1. Find unconditional Love.
2. She'll Love you furever!
3. He'll always listen.
4. Meet your new BFF

You're almost there 318 W Harrowgate Ln
Open 10 - 7/Tues-Sat

The dimensions for the sign are 24" wide and 18" high

Every week we will have a different picture of a different dog (hopefully last week's dog gets adopted). Anyhow, I am printing out yard signs, meaning that instead of printing 160 different signs it would be ideal just to replace the photo. So far the copy that is permanent is: "You're almost there. 318 W. Harrowgate Ln."

I could silhouette the image of the dog as well and super impose it on the sign, that's also a consideration, but ideally if I could have 4 tag lines I could print 40 signs of each and just replace the photo manually each week from my printer that would save costs.
Updates

Not enough designs to chose from and I edited the brief and committed to pay no matter what to increase the amount of designs as per your suggestions.

Target Market(s)

Animal lovers

Industry/Entity Type

Campaign

Font styles to use
Sans Serif

Colors

Designer to choose colors to be used in the design.

Requirements
Must have
• The dimensions for the sign are 24" wide and 18" high
Nice to have
• I want the signs to be hip, they should have a positive feel to them. You can alter the photos if you like. I am even open to new copy if you think something else works better.

```html
<!DOCTYPE html>
<html lang="en">
<head>
<meta charset="utf-8">
<title>Meet Your New BFF – Shelter Yard Sign</title>
<link rel="stylesheet" href="https://fonts.googleapis.com/css2?family=Fira+Sans+Extra+Condensed:wght@300;400;600;700;900&display=swap">
<style>
  :root {
    --page-bg: #e2e2e2;
    --sign-white: #ffffff;
    --ink: #0d0d0d;
    --charcoal: #2e2e2e;
    --sun-yellow: #fdc600;
    --photo-light: #b9b3ad;
    --photo-warm: #a0703a;
    --photo-dark: #3a2b1e;
  }
  * { margin: 0; padding: 0; box-sizing: border-box; }
  html, body {
    width: 1038px;
    height: 1200px;
    overflow: hidden;
    background: var(--page-bg);
  }
  .yard-sign {
    position: absolute;
    left: 24px;
    top: 229px;
    width: 990px;
    height: 742px;
    background: var(--sign-white);
    overflow: hidden;
    font-family: "Fira Sans Extra Condensed", "Arial Narrow", sans-serif;
    color: var(--ink);
  }
  .sign-art {
    position: absolute;
    inset: 0;
    width: 990px;
    height: 742px;
  }
  .tagline-lead {
    position: absolute;
    right: 56px;
    top: 40px;
    font-size: 88px;
    font-weight: 400;
    line-height: 1;
    letter-spacing: -1px;
    white-space: nowrap;
  }
  .tagline-band {
    position: absolute;
    left: 526px;
    top: 122px;
    width: 464px;
    height: 122px;
    background: var(--sun-yellow);
  }
  .tagline-main {
    position: absolute;
    right: 36px;
    top: 124px;
    font-size: 128px;
    font-weight: 900;
    line-height: 1;
    letter-spacing: -1px;
    white-space: nowrap;
  }
  .almost-there {
    position: absolute;
    right: 50px;
    top: 292px;
    text-align: right;
    font-size: 78px;
    font-weight: 300;
    line-height: 0.9;
    letter-spacing: -1px;
    white-space: nowrap;
  }
  .address-bar {
    position: absolute;
    left: 577px;
    top: 436px;
    width: 376px;
    height: 58px;
    background: var(--charcoal);
    color: var(--sun-yellow);
    display: flex;
    align-items: center;
    justify-content: center;
    gap: 10px;
    font-size: 40px;
    font-weight: 600;
    white-space: nowrap;
  }
  .address-bar svg { width: 24px; height: 34px; flex: none; }
  .opening-hours {
    position: absolute;
    right: 48px;
    top: 503px;
    display: flex;
    align-items: center;
    gap: 10px;
    font-size: 38px;
    font-weight: 600;
    color: var(--charcoal);
    white-space: nowrap;
  }
  .opening-hours svg { width: 32px; height: 32px; }
  .turn-pill {
    position: absolute;
    left: 601px;
    top: 632px;
    width: 331px;
    height: 60px;
    border-radius: 30px;
    background: var(--charcoal);
    color: var(--sun-yellow);
    display: flex;
    align-items: center;
    justify-content: center;
    font-size: 44px;
    font-weight: 600;
    white-space: nowrap;
  }
</style>
</head>
<body>
  <div class="yard-sign">
    <svg class="sign-art" viewBox="0 0 990 742">
      <defs>
        <linearGradient id="dogTones" x1="0" y1="0" x2="1" y2="1">
          <stop offset="0" stop-color="var(--photo-light)"/>
          <stop offset="0.45" stop-color="var(--photo-warm)"/>
          <stop offset="1" stop-color="var(--photo-dark)"/>
        </linearGradient>
      </defs>

      <path class="swoosh-band" fill="var(--sun-yellow)"
            d="M598 244 H622 C615 420 470 560 485 742 H400 C420 570 590 430 598 244 Z"/>

      <path class="dog-photo" role="img" aria-label="Photo of this week's featured shelter dog"
            fill="url(#dogTones)"
            d="M0 0 H509 C580 60 610 160 597 250 C578 420 420 540 381 742 H0 Z"/>

      <path class="swoosh-edge" fill="none" stroke="var(--charcoal)" stroke-width="9"
            d="M509 0 C580 60 610 160 597 250"/>
      <path class="swoosh-line" fill="none" stroke="var(--charcoal)" stroke-width="3"
            d="M607 252 C590 430 440 560 408 742"/>

      <g class="direction-chevrons" fill="none" stroke="var(--charcoal)" stroke-width="7">
        <polyline points="490,630 510,662 490,696"/>
        <polyline points="504,630 524,662 504,696"/>
        <polyline points="518,630 538,662 518,696"/>
        <polyline points="532,630 552,662 532,696"/>
        <polyline points="546,630 566,662 546,696"/>
        <polyline points="560,630 580,662 560,696"/>
        <polyline points="574,630 594,662 574,696"/>
        <polyline points="934,630 954,662 934,696"/>
        <polyline points="948,630 968,662 948,696"/>
      </g>
      <g class="direction-stripes" stroke="var(--charcoal)" stroke-width="6" stroke-dasharray="4 4">
        <line x1="600" y1="627" x2="932" y2="627"/>
        <line x1="600" y1="698" x2="932" y2="698"/>
      </g>
    </svg>

    <div class="tagline-band"></div>
    <div class="tagline-lead">MEET YOUR</div>
    <div class="tagline-main">NEW BFF</div>

    <div class="almost-there">You're<br>Almost There</div>

    <div class="address-bar">
      <svg viewBox="0 0 24 34" aria-hidden="true">
        <path d="M12 1C5.9 1 1 5.9 1 12c0 8 11 21 11 21s11-13 11-21C23 5.9 18.1 1 12 1z" fill="var(--sun-yellow)"/>
        <circle cx="12" cy="12" r="4.5" fill="var(--charcoal)"/>
      </svg>
      <span>318 W Harrowgate Ln</span>
    </div>

    <div class="opening-hours">
      <svg viewBox="0 0 32 32" aria-hidden="true">
        <circle cx="16" cy="18" r="11" fill="none" stroke="var(--charcoal)" stroke-width="2.5"/>
        <path d="M16 11v7l4 3" fill="none" stroke="var(--charcoal)" stroke-width="2.5" stroke-linecap="round"/>
        <path d="M4 8l5-5M28 8l-5-5" stroke="var(--charcoal)" stroke-width="3" stroke-linecap="round"/>
      </svg>
      <span>Open 10 - 7/Tues-Sat</span>
    </div>

    <div class="turn-pill">TURN RIGHT</div>
  </div>
</body>
</html>
```